Stationery Design Project

We need a stationery design for a new business consulting business based in New Zealand.
We have the logo and business cards designed and we're looking for letterhead, compliments slip and PowerPoint presentation format that aligns with our business cards.
Industry/Entity Type
Business
Requirements
Must have
- same colors and format as business cards

```html
<!DOCTYPE html>
<html lang="en">
<head>
<meta charset="utf-8">
<title>Presentation Heading Page – Agenda</title>
<link rel="stylesheet" href="https://fonts.googleapis.com/css2?family=Arimo:wght@400;700&family=PT+Sans+Narrow&display=swap">
<style>
  :root {
    --frame-grey: #b3b3b3;
    --sheet-white: #ffffff;
    --label-red: #e3222b;
    --brand-green: #78b828;
    --band-grey: #a3a3a3;
    --ink: #232323;
    --bullet-grey: #9a9a9a;
    --wordmark-grey: #9b9b9b;
    --slide-top: #f8f9ec;
    --slide-bottom: #e9f1f8;
    --slide-edge: #8c8c8c;
  }
  html, body {
    margin: 0;
    padding: 0;
    width: 1200px;
    height: 849px;
    overflow: hidden;
    background: var(--frame-grey);
  }
  .sheet {
    position: absolute;
    left: 17px;
    top: 17px;
    width: 1163px;
    height: 812px;
    background: var(--sheet-white);
  }
  .sheet-label {
    position: absolute;
    left: 85px;
    top: 62px;
    margin: 0;
    font-family: "PT Sans Narrow", sans-serif;
    font-weight: 400;
    font-size: 25px;
    letter-spacing: -0.3px;
    color: var(--label-red);
  }
  .slide {
    position: absolute;
    left: 147px;
    top: 119px;
    width: 866px;
    height: 649px;
    background: linear-gradient(to bottom, var(--slide-top), var(--slide-bottom));
    outline: 1px solid var(--slide-edge);
    box-shadow: 9px 9px 10px rgba(0, 0, 0, 0.45);
    overflow: hidden;
    font-family: "Arimo", sans-serif;
  }
  .agenda-title {
    position: absolute;
    left: 82px;
    top: 119px;
    margin: 0;
    font-size: 26px;
    font-weight: 700;
    letter-spacing: 2.5px;
    color: var(--brand-green);
  }
  .divider {
    position: absolute;
    left: 362px;
    top: 106px;
    width: 2px;
    height: 386px;
    background: var(--brand-green);
  }
  .agenda-list {
    position: absolute;
    left: 421px;
    top: 124px;
    margin: 0;
    padding: 0;
    list-style: none;
  }
  .agenda-list li {
    position: relative;
    height: 56.2px;
    padding-left: 31px;
    font-size: 19px;
    font-weight: 700;
    letter-spacing: 1.6px;
    color: var(--ink);
    line-height: 30px;
  }
  .agenda-list li::before {
    content: "";
    position: absolute;
    left: 0;
    top: 13px;
    width: 5px;
    height: 5px;
    border-radius: 50%;
    background: var(--bullet-grey);
  }
  .wordmark {
    position: absolute;
    left: 80px;
    top: 580px;
    margin: 0;
    font-family: "Arimo", sans-serif;
    font-size: 25px;
    font-weight: 400;
    letter-spacing: -0.5px;
    color: var(--wordmark-grey);
  }
  .footer-band {
    position: absolute;
    left: 0;
    top: 0;
  }
</style>
</head>
<body>
  <div class="sheet">
    <p class="sheet-label">&gt; Power Point Heading Pages</p>

    <section class="slide">
      <svg class="footer-band" width="866" height="649" viewBox="0 0 866 649" aria-hidden="true">
        <polygon points="0,649 866,574 866,631" fill="var(--brand-green)"/>
        <polygon points="0,649 866,631 866,649" fill="var(--band-grey)"/>
      </svg>

      <h1 class="agenda-title">AGENDA</h1>
      <div class="divider"></div>

      <ul class="agenda-list">
        <li>FINANCIAL PERFORMANCE</li>
        <li>CUSTOMER SATISFACTION</li>
        <li>HR</li>
        <li>DEBTORS</li>
        <li>REDEVELOPMENT</li>
        <li>STAFF MAGAZINE</li>
        <li>ANY QUESTIONS</li>
      </ul>

      <p class="wordmark">Tarn Consulting</p>
    </section>
  </div>
</body>
</html>
```